standardize print collateral

we need help standardizing all print collateral and website. top priorities:

1. standardized case studies template
2. standardized marketing slicks template
3. standardized powerpoint template
Updates

Project Deadline Extended
Reason: We are extending the project to allow current design submissions to be tweaked while providing the opportunity for new designs to be submitted. We will need all 3 collateral designs submitted to make a final decision. Please note, these 3 designs should all look different, needless to say they should all compliment eachother. As for some direction, the powerpoint main color should not be yellow since yellow does not show up the same shade on any screen. The case study and marketing slicks will be printed and often sit next to our competitors marketing material - think high end product, technology, revolutionary, edgy, professional. The designs should compliment eachother and feel like the Brightfern Metrics brand (which you are determining) and should stand out professionally. We are open to introducing new colors into our brand, the only thing that must remain the same is our logo. Have fun, make it edgy, and keep it professional. Looking forward to seeing what you submit!

Target Market(s)

Property Casualty Insurance Companies: Executive level wording with actuarial credibility

Industry/Entity Type

Marketing

Requirements
Must have
• professional layout for existing collateral and 2-page marketing slicks. style guide/colors can be transferred to powerpoint. logo must stay; everything else (i.e. color, font, layout/structure etc.) is flexible. The three components should not looks the same, they should only compliment eachother.
Nice to have
• we are revolutionizing a conservative industry, so adequate level of edgy/advanced technology/impactful feel to layout
Should not have
• no need to stay within color constraints of yellow, but need to appropriately work well with the eagle head logo

```html
<!DOCTYPE html>
<html lang="en">
<head>
<meta charset="utf-8">
<title>Brightfern Metrics – Corvane Slick</title>
<link href="https://fonts.googleapis.com/css2?family=Arimo:wght@400;700&family=Carlito:wght@400;700&display=swap" rel="stylesheet">
<style>
  :root{
    --ink:#111111;
    --text:#2b2b2b;
    --muted:#555555;
    --gold:#f2b01e;
    --frame:#c9c9c9;
    --bar:#4f81bd;
    --grid:#d9d9d9;
    --paper:#ffffff;
  }
  *{margin:0;padding:0;box-sizing:border-box}
  html,body{width:847px;height:1200px;overflow:hidden;background:var(--paper)}
  body{font-family:"Carlito",Calibri,sans-serif;color:var(--text);position:relative}
  .header-swoosh{position:absolute;left:0;top:0;width:847px;height:160px}
  .headline{position:absolute;top:252px;left:0;width:847px;text-align:center;font-size:19px;line-height:26px;color:var(--ink)}
  .panel-frame{position:absolute;left:74px;top:336px;width:706px;height:603px;border:1.5px solid var(--frame)}
  .panel-frame .v-rule{position:absolute;left:352px;top:0;width:1.5px;height:326px;background:var(--frame)}
  .panel-frame .h-rule{position:absolute;left:0;top:326px;width:100%;height:1.5px;background:var(--frame)}
  .chart{position:absolute}
  .chart-title{font-family:"Carlito",Calibri,sans-serif;font-size:15px;font-weight:700;fill:var(--ink)}
  .axis-label{font-family:"Carlito",Calibri,sans-serif;font-size:6.5px;fill:#444}
  .axis-name{font-family:"Carlito",Calibri,sans-serif;font-size:6.5px;font-weight:700;fill:#444}
  .caption{position:absolute;font-family:"Arimo",Arial,sans-serif;font-size:14.5px;line-height:16px;color:var(--muted)}
  .caption.justify{text-align:justify}
  .report-note{position:absolute;left:112px;top:688px;width:630px;text-align:center;font-family:"Arimo",Arial,sans-serif;font-size:14.5px;line-height:19px;color:var(--muted)}
  .closing{position:absolute;top:978px;left:0;width:847px;text-align:center;font-size:17px;line-height:25px;color:var(--ink)}
  .about{position:absolute;top:1054px;left:74px;width:710px;font-size:14px;line-height:21px;color:var(--muted)}
  .footer-rule{position:absolute;left:43px;top:1106px;width:782px;height:1.5px;background:var(--gold)}
  .footer{position:absolute;top:1111px;left:0;width:847px;text-align:center;font-size:13.5px;line-height:18px;color:var(--ink)}
  .footer .company{font-size:15px}
</style>
</head>
<body>
  <svg class="header-swoosh" viewBox="0 0 847 160" aria-hidden="true">
    <path d="M0 0 H847 V8 C620 20 300 40 120 90 C70 105 30 125 0 150 Z" fill="var(--gold)"/>
    <path d="M0 0 H847 C640 0 330 10 150 55 C90 72 40 95 0 130 Z" fill="var(--ink)"/>
  </svg>

  <p class="headline">Corvane detects, measures and presents actionable options to correct the<br>effects of adverse selection within any P&amp;C portfolio.</p>

  <div class="panel-frame">
    <div class="v-rule"></div>
    <div class="h-rule"></div>
  </div>

  <svg class="chart" style="left:92px;top:352px" width="306" height="175" viewBox="0 0 306 175">
    <text class="chart-title" x="153" y="14" text-anchor="middle">Underwriting Score</text>
    <g stroke="var(--grid)" stroke-width="0.7">
      <line x1="40" y1="35" x2="300" y2="35"/><line x1="40" y1="50" x2="300" y2="50"/>
      <line x1="40" y1="65" x2="300" y2="65"/><line x1="40" y1="80" x2="300" y2="80"/>
      <line x1="40" y1="95" x2="300" y2="95"/><line x1="40" y1="110" x2="300" y2="110"/>
      <line x1="40" y1="125" x2="300" y2="125"/><line x1="40" y1="140" x2="300" y2="140"/>
    </g>
    <line x1="40" y1="155" x2="300" y2="155" stroke="#999" stroke-width="0.8"/>
    <g class="axis-label" text-anchor="end">
      <text x="36" y="37">80%</text><text x="36" y="52">70%</text><text x="36" y="67">60%</text>
      <text x="36" y="82">50%</text><text x="36" y="97">40%</text><text x="36" y="112">30%</text>
      <text x="36" y="127">20%</text><text x="36" y="142">10%</text><text x="36" y="157">0%</text>
    </g>
    <g fill="var(--bar)">
      <rect x="52" y="52" width="18" height="103"/>
      <rect x="95" y="82" width="18" height="73"/>
      <rect x="138" y="108" width="18" height="47"/>
      <rect x="181" y="113" width="18" height="42"/>
      <rect x="224" y="125" width="18" height="30"/>
      <rect x="267" y="129" width="18" height="26"/>
    </g>
    <g class="axis-label" text-anchor="middle">
      <text x="61" y="164">0-99</text><text x="104" y="164">99-249</text><text x="147" y="164">250-499</text>
      <text x="190" y="164">500-749</text><text x="233" y="164">750-899</text><text x="276" y="164">900-1000</text>
    </g>
    <text class="axis-name" x="170" y="173" text-anchor="middle">Score Tier</text>
    <text class="axis-name" transform="translate(14 96) rotate(-90)" text-anchor="middle">Loss Ratio</text>
  </svg>
  <p class="caption justify" style="left:111px;top:534px;width:273px">Discover the pricing imbalances within the portfolio. These imbalances are the main driver of the adverse selection</p>

  <svg class="chart" style="left:440px;top:352px" width="320" height="175" viewBox="0 0 320 175">
    <defs>
      <radialGradient id="bubble" cx="40%" cy="35%" r="65%">
        <stop offset="0" stop-color="#e6eef9"/><stop offset="1" stop-color="#8eaad6"/>
      </radialGradient>
    </defs>
    <text class="chart-title" x="160" y="14" text-anchor="middle">Trend and Loss Ratio</text>
    <g stroke="var(--grid)" stroke-width="0.7">
      <line x1="42" y1="40" x2="310" y2="40"/><line x1="42" y1="57" x2="310" y2="57"/>
      <line x1="42" y1="74" x2="310" y2="74"/><line x1="42" y1="91" x2="310" y2="91"/>
      <line x1="42" y1="108" x2="310" y2="108"/><line x1="42" y1="125" x2="310" y2="125"/>
    </g>
    <line x1="42" y1="142" x2="310" y2="142" stroke="#999" stroke-width="0.8"/>
    <line x1="176" y1="40" x2="176" y2="142" stroke="#999" stroke-width="0.8"/>
    <g class="axis-label" text-anchor="end">
      <text x="38" y="42">60%</text><text x="38" y="59">50%</text><text x="38" y="76">40%</text>
      <text x="38" y="93">30%</text><text x="38" y="110">20%</text><text x="38" y="127">10%</text><text x="38" y="144">0%</text>
    </g>
    <g class="axis-label" text-anchor="middle">
      <text x="42" y="152">-40%</text><text x="109" y="152">-20%</text><text x="176" y="152">0%</text>
      <text x="243" y="152">20%</text><text x="310" y="152">40%</text>
    </g>
    <line x1="42" y1="74" x2="290" y2="74" stroke="var(--bar)" stroke-width="1.2"/>
    <text class="axis-label" x="292" y="76">40%</text>
    <g stroke="#fff" stroke-width="0.8" fill="url(#bubble)">
      <circle cx="250" cy="56" r="12"/>
      <circle cx="136" cy="70" r="11"/>
      <circle cx="126" cy="86" r="12"/>
      <circle cx="112" cy="103" r="12"/>
    </g>
    <g class="axis-label" text-anchor="middle">
      <text x="250" y="58">1</text><text x="136" y="72">3</text><text x="126" y="88">4</text><text x="112" y="105">2</text>
    </g>
    <text class="axis-name" x="176" y="162" text-anchor="middle">Growth/Decline</text>
    <text class="axis-name" transform="translate(14 91) rotate(-90)" text-anchor="middle">Loss Ratio</text>
  </svg>
  <p class="caption justify" style="left:470px;top:532px;width:268px">Show trends within the portfolio in real time covering premium adequacy and the quality of all business being written.</p>

  <p class="report-note">Report on detailed analyses including sales trend and profitability trends.&nbsp; This allows for a method of managing distribution channels while addressing pricing imbalances.</p>

  <svg class="chart" style="left:92px;top:752px" width="320" height="175" viewBox="0 0 320 175">
    <text class="chart-title" x="140" y="14" text-anchor="middle">Portfolio Exposure</text>
    <g class="axis-label" text-anchor="end">
      <text x="28" y="38">550</text><text x="28" y="50">540</text><text x="28" y="62">530</text>
      <text x="28" y="74">520</text><text x="28" y="86">510</text><text x="28" y="98">500</text>
      <text x="28" y="110">490</text><text x="28" y="122">480</text><text x="28" y="134">470</text><text x="28" y="146">460</text>
    </g>
    <line x1="32" y1="144" x2="290" y2="144" stroke="#999" stroke-width="0.8"/>
    <polyline fill="none" stroke="var(--bar)" stroke-width="1.4"
      points="34,66 42,58 50,60 58,66 66,64 74,50 82,52 90,58 98,56 106,48 114,50 122,60 130,60 138,50 146,52 154,60 162,66 170,58 178,56 186,66 194,72 202,68 210,72 218,90 226,94 234,88 242,88 250,96 258,96 266,88 274,92 282,98 290,100"/>
    <g class="axis-label" text-anchor="end">
      <text transform="translate(40 150) rotate(-90)">01/2012</text>
      <text transform="translate(72 150) rotate(-90)">04/2012</text>
      <text transform="translate(104 150) rotate(-90)">07/2012</text>
      <text transform="translate(136 150) rotate(-90)">10/2012</text>
      <text transform="translate(168 150) rotate(-90)">01/2013</text>
      <text transform="translate(200 150) rotate(-90)">04/2013</text>
      <text transform="translate(232 150) rotate(-90)">07/2013</text>
      <text transform="translate(264 150) rotate(-90)">10/2013</text>
    </g>
    <text class="axis-name" transform="translate(8 90) rotate(-90)" text-anchor="middle">Portfolio Score</text>
  </svg>

  <svg class="chart" style="left:440px;top:752px" width="320" height="175" viewBox="0 0 320 175">
    <text class="chart-title" x="170" y="18" text-anchor="middle">Premium Change</text>
    <g class="axis-label" text-anchor="end">
      <text x="46" y="38">60%</text><text x="46" y="55">40%</text><text x="46" y="72">20%</text>
      <text x="46" y="89">0%</text><text x="46" y="106">-20%</text><text x="46" y="123">-40%</text>
      <text x="46" y="140">-60%</text><text x="46" y="157">-80%</text>
    </g>
    <g stroke="var(--grid)" stroke-width="0.7">
      <line x1="50" y1="36" x2="300" y2="36"/><line x1="50" y1="53" x2="300" y2="53"/>
      <line x1="50" y1="70" x2="300" y2="70"/><line x1="50" y1="104" x2="300" y2="104"/>
      <line x1="50" y1="121" x2="300" y2="121"/><line x1="50" y1="138" x2="300" y2="138"/><line x1="50" y1="155" x2="300" y2="155"/>
    </g>
    <line x1="50" y1="87" x2="300" y2="87" stroke="#999" stroke-width="0.8"/>
    <g fill="var(--bar)">
      <rect x="69" y="87" width="18" height="6"/>
      <rect x="131" y="87" width="18" height="52"/>
      <rect x="193" y="45" width="18" height="42"/>
      <rect x="255" y="66" width="18" height="21"/>
    </g>
    <g class="axis-label" text-anchor="middle">
      <text x="78" y="96">1</text><text x="140" y="96">2</text><text x="202" y="96">3</text><text x="264" y="96">4</text>
    </g>
    <text class="axis-name" x="175" y="166" text-anchor="middle">Segment Number</text>
    <text class="axis-name" transform="translate(20 96) rotate(-90)" text-anchor="middle">% Change</text>
  </svg>

  <p class="closing">Through the use of these advanced analytics your company has the<br>opportunity to future proof each of your portfolios.</p>

  <p class="about">Brightfern Metrics provides breakthrough predictive analytics powered by machine learning and the latest statistical techniques, enabling property and casualty insurers to achieve superior performance.</p>

  <div class="footer-rule"></div>
  <div class="footer">
    <p class="company">Brightfern Metrics</p>
    <p>218 Meridian Avenue, Suite 410, Greenvale, SC 29000, Phone: 555.214.3380, Fax: 555.214.3391</p>
    <p>www.brightfernmetrics.com</p>
  </div>
</body>
</html>
```